I am a highly experienced private practice psychotherapist serving high end clientele in the Wall Street area of New York City. I need electronic letterhead (that can also be printed) to use for bills, receipts, and correspondences.

My clients are very high end and are used to elegance and wealth. The letterhead should contain the following information: Marian T. Holcombe, LCSW 72 Pellham Street, Suite 2561 New York, NY 10087 Phone : (917) 555-3194 email: therapy@marianholcombelcsw.example website: www.marianholcombelcsw.example

Thank you for your designs. Please be advised that the letterhead will be used for bills/invoices; professional letters to other mental health professionals and doctors, as well as to attorneys. It needs to be highly professional in the same way that a law firm has professional and elegant letterhead, raher than whimsical or with spa designers. My letters end up as official documents.

```html
<!DOCTYPE html>
<html lang="en">
<head>
<meta charset="utf-8">
<title>Marian T. Holcombe, LCSW — Letterhead</title>
<link rel="stylesheet" href="https://fonts.googleapis.com/css2?family=Jost:wght@500;600&family=Open+Sans:wght@400;700&display=swap">
<style>
  :root {
    --plum: #951a7f;
    --ink: #000000;
    --paper: #ffffff;
  }
  * { margin: 0; padding: 0; box-sizing: border-box; }
  html, body {
    width: 927px;
    height: 1200px;
    overflow: hidden;
    background: var(--paper);
  }
  .letterhead {
    position: relative;
    width: 927px;
    height: 1200px;
    background: var(--paper);
    overflow: hidden;
  }
  .header-wave {
    position: absolute;
    left: 0;
    top: 0;
    width: 927px;
    height: 242px;
  }
  .contact-list {
    position: absolute;
    left: 40px;
    top: 16px;
    list-style: none;
    font-family: "Jost", sans-serif;
    font-weight: 600;
    font-size: 14.5px;
    color: var(--ink);
  }
  .contact-item {
    display: flex;
    align-items: center;
    height: 28px;
  }
  .contact-icon {
    width: 22px;
    height: 22px;
    margin-right: 14px;
    flex: none;
  }
  .contact-item.phone .contact-text { margin-left: 18px; }
  .contact-item.phone .contact-icon { margin-right: 0; }
  .practitioner {
    position: absolute;
    right: 44px;
    top: 20px;
    text-align: right;
    font-family: "Open Sans", sans-serif;
    color: var(--ink);
  }
  .practitioner-name {
    font-weight: 700;
    font-size: 26px;
    line-height: 32px;
    letter-spacing: -0.2px;
  }
  .practitioner-credential {
    font-weight: 400;
    font-size: 16px;
    line-height: 18px;
  }
  .footer-band {
    position: absolute;
    left: 0;
    bottom: 0;
    width: 927px;
  }
  .footer-band .rule {
    height: 12px;
    background: var(--ink);
  }
  .footer-band .fill {
    height: 26px;
    background: var(--plum);
  }
</style>
</head>
<body>
<div class="letterhead">
  <svg class="header-wave" viewBox="0 0 612 160" preserveAspectRatio="none" aria-hidden="true">
    <path fill="var(--plum)" d="M0,78 C120,96 260,100 612,44 L612,78 C420,100 260,106 160,101 C80,97 30,89 0,83 Z"/>
    <path fill="var(--ink)" d="M0,84 C60,100 150,110 260,106 C400,101 520,88 612,79 L612,85 C520,93 400,107 260,111 C150,114 60,106 0,91 Z"/>
  </svg>

  <ul class="contact-list">
    <li class="contact-item phone">
      <svg class="contact-icon" viewBox="0 0 24 24" aria-hidden="true">
        <rect x="3" y="3" width="18" height="18" rx="4" fill="var(--ink)"/>
        <path d="M9 7.5c-1 .6-1.6 1.6-1.2 3 .8 2.7 2.9 4.8 5.6 5.6 1.4.4 2.4-.2 3-1.2l-1.8-1.5-1.3.9c-1.2-.6-2.1-1.5-2.7-2.7l.9-1.3z" fill="var(--paper)"/>
      </svg>
      <span class="contact-text">(917) 555-3194</span>
    </li>
    <li class="contact-item address">
      <svg class="contact-icon" viewBox="0 0 24 24" aria-hidden="true">
        <path d="M12 2a7 7 0 0 0-7 7c0 5.2 7 13 7 13s7-7.8 7-13a7 7 0 0 0-7-7zm0 9.8a2.8 2.8 0 1 1 0-5.6 2.8 2.8 0 0 1 0 5.6z" fill="var(--ink)"/>
      </svg>
      <span class="contact-text">72 Pellham Street, Suite 2561 New York, NY 10087</span>
    </li>
    <li class="contact-item website">
      <svg class="contact-icon" viewBox="0 0 24 24" aria-hidden="true">
        <g fill="none" stroke="var(--ink)" stroke-width="1.8">
          <circle cx="11" cy="11" r="8.5"/>
          <ellipse cx="11" cy="11" rx="3.6" ry="8.5"/>
          <path d="M2.5 11h17M4 6.5h14M4 15.5h14"/>
        </g>
        <path d="M14 14l7 3-3 1-1 3z" fill="var(--ink)"/>
      </svg>
      <span class="contact-text">www.marianholcombelcsw.example</span>
    </li>
    <li class="contact-item email">
      <svg class="contact-icon" viewBox="0 0 24 24" aria-hidden="true">
        <g fill="none" stroke="var(--ink)" stroke-width="1.6">
          <rect x="2" y="5" width="20" height="14"/>
          <path d="M2 5l10 8 10-8M2 19l7.5-7M22 19l-7.5-7"/>
        </g>
      </svg>
      <span class="contact-text">therapy@marianholcombelcsw.example</span>
    </li>
  </ul>

  <div class="practitioner">
    <div class="practitioner-name">Marian T. Holcombe</div>
    <div class="practitioner-credential">LCSW</div>
  </div>

  <div class="footer-band" aria-hidden="true">
    <div class="rule"></div>
    <div class="fill"></div>
  </div>
</div>
</body>
</html>
```